Yard Sign Design Needed

Yard sign needed for mowing & landscaping company. Would like to use the top logo with black background which is attached. Would like MOWING to be in large standout letters. The word "landscaping" can be smaller and more artistic or omitted. Will need room for phone number once design is approved. The phone number will need to stand out and look identical/similar to the word 'MOWING"

```html
<!DOCTYPE html>
<html lang="en">
<head>
<meta charset="utf-8">
<title>Halden Contractors – Mowing Yard Sign</title>
<link href="https://fonts.googleapis.com/css2?family=Saira:wdth,wght@50..125,100..900&display=swap" rel="stylesheet">
<style>
  :root {
    --page: #ffffff;
    --ink: #060707;
    --lime: #cfe02b;
    --leaf: #8cc63f;
    --phone-green: #a9d04c;
    --brand-green: #8fb43a;
    --white: #ffffff;
  }
  html, body {
    margin: 0;
    padding: 0;
    width: 989px;
    height: 1200px;
    overflow: hidden;
    background: var(--page);
  }
  .canvas {
    position: relative;
    width: 989px;
    height: 1200px;
    font-family: "Saira", "Arial Black", sans-serif;
    font-stretch: 125%;
    font-variation-settings: "wdth" 125;
  }
  .yard-sign {
    position: absolute;
    left: 145px;
    top: 248px;
    width: 698px;
    height: 349px;
    display: flex;
    flex-direction: column;
    box-shadow: 0 4px 6px rgba(0,0,0,0.15);
  }
  .brand-band {
    height: 125px;
    flex: none;
    background: var(--ink);
    display: flex;
    align-items: center;
    justify-content: center;
    gap: 20px;
  }
  .brand-mark {
    width: 52px;
    height: 52px;
    background: var(--brand-green);
  }
  .brand-name {
    color: var(--brand-green);
    font-weight: 700;
    line-height: 1;
    text-transform: uppercase;
    display: flex;
    flex-direction: column;
    align-items: center;
    gap: 8px;
  }
  .brand-name .brand-main { font-size: 54px; letter-spacing: 2px; }
  .brand-name .brand-sub { font-size: 24px; letter-spacing: 0.5px; }
  .service-band {
    height: 144px;
    flex: none;
    background:
      radial-gradient(ellipse at 68% 20%, var(--leaf) 0%, rgba(140,198,63,0) 60%),
      linear-gradient(100deg, var(--lime) 0%, #a8d23a 45%, #94ca3f 65%, var(--lime) 100%);
    display: flex;
    flex-direction: column;
    align-items: center;
    justify-content: center;
  }
  .service-main {
    margin: 0;
    color: var(--white);
    font-weight: 800;
    font-size: 112px;
    line-height: 0.85;
    letter-spacing: 0;
    text-shadow: 3px 4px 4px rgba(0,0,0,0.35);
  }
  .service-sub {
    margin: 6px 0 0;
    color: var(--white);
    font-weight: 800;
    font-size: 28px;
    line-height: 1;
    letter-spacing: 12px;
    padding-left: 12px;
  }
  .phone-band {
    height: 80px;
    flex: none;
    background: var(--ink);
    display: flex;
    align-items: center;
    justify-content: center;
  }
  .phone-number {
    color: var(--phone-green);
    font-weight: 800;
    font-size: 58px;
    line-height: 1;
    letter-spacing: 0;
    word-spacing: 4px;
  }
</style>
</head>
<body>
<main class="canvas">
  <section class="yard-sign" aria-label="Mowing and landscaping yard sign">
    <header class="brand-band">
      <span class="brand-mark" aria-hidden="true"></span>
      <div class="brand-name">
        <span class="brand-main">Halden</span>
        <span class="brand-sub">Contractors LLC</span>
      </div>
    </header>
    <div class="service-band">
      <h1 class="service-main">MOWING</h1>
      <p class="service-sub">LANDSCAPING</p>
    </div>
    <footer class="phone-band">
      <span class="phone-number">55 240 718 36</span>
    </footer>
  </section>
</main>
</body>
</html>
```